Austrian finance und insurance broker needs business card design

We Need a serious looking Design for Business Card. we consult private and corporates customers in finance and insurance questions. the final design should express security and experience. We consult customers in questions of loans, Investments and insurance and have a wide range of Banks to offer. We compare several offers and select the best for our customers.

Target Market(s)

private and coporate customers with efforts in Money and insurance

Industry/Entity Type

Insurance Broker

Contact Information for Business Card

Bernhard Aigner
Geschäftsführer
staatl. geprüfter Vermögensberater und Versicherungsmakler
Tel: 0664 521 8409
office@der-brandl.at
www.der-brandl.at
Leopold Hainz Gasse 14
2183 Melkstetten
GISA Nr. 48270315 u. 51736048 (backside)

Font styles to use
Serif
Sans Serif

Requirements
Must have
• logo (designcrowd zip) and all Details
Nice to have
• makler logo design, maybe a 2 coloured Version is possible

```html
<!DOCTYPE html>
<html lang="de">
<head>
<meta charset="utf-8">
<title>Aigner Vermögensberatung – Visitenkarte</title>
<link rel="stylesheet" href="https://fonts.googleapis.com/css2?family=Lexend:wght@300;400;500;600&display=swap">
<style>
  :root {
    --stage: #1c1c1e;
    --paper: #f4f4f3;
    --brand-blue: #2f5cb3;
    --brand-blue-deep: #234a9c;
    --ink: #4a4a4c;
    --ink-soft: #6a6a6d;
    --badge-red: #c8283a;
    --white: #ffffff;
  }
  * { box-sizing: border-box; margin: 0; padding: 0; }
  html, body { width: 1200px; height: 960px; overflow: hidden; }
  body {
    background: var(--stage);
    font-family: "Lexend", sans-serif;
    position: relative;
  }
  .card {
    position: absolute;
    width: 560px;
    height: 362px;
    border-radius: 3px;
    overflow: hidden;
    box-shadow: 0 18px 40px rgba(0,0,0,.55);
  }

  /* ---------- back side (blue) ---------- */
  .card--back {
    left: 580px; top: 60px;
    background: linear-gradient(160deg, var(--brand-blue-deep), var(--brand-blue));
    color: var(--white);
  }
  .card--back .lockup {
    position: absolute; left: 70px; top: 92px;
    display: flex; align-items: center; gap: 22px;
  }
  .card--back .lockup-mark {
    width: 96px; height: 96px; border-radius: 50%;
    border: 4px solid var(--white);
    flex: none;
  }
  .card--back .lockup-divider {
    width: 2px; height: 118px; background: rgba(255,255,255,.85);
  }
  .card--back .company-name { font-size: 27px; font-weight: 500; line-height: 1.15; }
  .card--back .company-name small { font-size: 19px; }
  .card--back .tagline { font-size: 17px; font-weight: 400; margin-top: 6px; }
  .partner-badge {
    position: absolute; left: 268px; top: 270px;
    width: 62px; height: 62px; border-radius: 50%;
    background: var(--badge-red);
    border: 3px solid var(--white);
  }

  /* ---------- front side (white) ---------- */
  .card--front {
    left: 80px; top: 480px;
    background: var(--paper);
    color: var(--ink);
  }
  .card--front .edge-band {
    position: absolute; left: 0; right: 0; bottom: 0; height: 26px;
    background: var(--brand-blue);
  }
  .card--front .lockup {
    position: absolute; left: 30px; top: 24px;
    display: flex; align-items: center; gap: 16px;
  }
  .card--front .lockup-mark {
    width: 66px; height: 66px; border-radius: 50%;
    border: 3px solid var(--brand-blue); flex: none;
  }
  .card--front .lockup-divider { width: 2px; height: 80px; background: var(--ink-soft); }
  .card--front .company-name {
    font-size: 19px; font-weight: 500; color: var(--brand-blue); line-height: 1.15;
  }
  .card--front .company-name small { font-size: 13px; }
  .card--front .tagline { font-size: 13px; font-weight: 500; color: var(--ink); margin-top: 3px; }

  .person {
    position: absolute; left: 30px; top: 128px;
    border-left: 3px solid var(--brand-blue);
    padding-left: 12px;
  }
  .person-name { font-size: 24px; font-weight: 600; color: var(--brand-blue); }
  .person-role, .person-qualification { font-size: 13px; font-weight: 300; color: var(--ink); line-height: 1.4; }

  .contact {
    position: absolute; left: 30px; top: 214px;
    border-left: 2px solid var(--ink-soft);
    padding-left: 12px;
    list-style: none;
    font-size: 13px; font-weight: 300; color: var(--ink); line-height: 1.45;
  }
  .contact li { display: flex; align-items: center; gap: 6px; }
  .contact svg { width: 11px; height: 11px; fill: var(--brand-blue); flex: none; }
  .contact .plain { padding-left: 17px; }
</style>
</head>
<body>

  <section class="card card--back" aria-label="Rückseite">
    <div class="lockup">
      <div class="lockup-mark" aria-hidden="true"></div>
      <div class="lockup-divider"></div>
      <div>
        <p class="company-name">Aigner Vermögensberatung <small>GmbH</small></p>
        <p class="tagline">Finanzieren, Versichern, Vorsorgen</p>
      </div>
    </div>
    <div class="partner-badge" role="img" aria-label="Partnerabzeichen"></div>
  </section>

  <section class="card card--front" aria-label="Vorderseite">
    <div class="lockup">
      <div class="lockup-mark" aria-hidden="true"></div>
      <div class="lockup-divider"></div>
      <div>
        <p class="company-name">Aigner Vermögensberatung <small>GmbH</small></p>
        <p class="tagline">Finanzieren, Versichern, Vorsorgen</p>
      </div>
    </div>

    <div class="person">
      <p class="person-name">Bernhard Aigner</p>
      <p class="person-role">Geschäftsführer</p>
      <p class="person-qualification">staatl. geprüfter Vermögensberater und Versicherungsmakler</p>
    </div>

    <ul class="contact">
      <li class="plain">Leopold Hainz Gasse 14, 2183 Melkstetten</li>
      <li class="plain">GISA Nr. 48270315 u. 51736048</li>
      <li>
        <svg viewBox="0 0 24 24" aria-hidden="true"><path d="M6.6 10.8a15.1 15.1 0 0 0 6.6 6.6l2.2-2.2c.3-.3.7-.4 1-.2 1.1.4 2.3.6 3.6.6.6 0 1 .4 1 1V20c0 .6-.4 1-1 1A17 17 0 0 1 3 4c0-.6.4-1 1-1h3.5c.6 0 1 .4 1 1 0 1.2.2 2.4.6 3.6.1.3 0 .7-.2 1z"/></svg>
        0664 521 8409
      </li>
      <li>
        <svg viewBox="0 0 24 24" aria-hidden="true"><path d="M2 5h20v14H2zm2 2v.5l8 5 8-5V7z"/></svg>
        office@der-brandl.at
      </li>
      <li>
        <svg viewBox="0 0 24 24" aria-hidden="true"><circle cx="12" cy="12" r="10"/></svg>
        www.der-brandl.at
      </li>
    </ul>

    <div class="edge-band"></div>
  </section>

</body>
</html>
```